1/2 Page add for BRMTL Conference

We are looking for a 1/2 page ad to support the annual BRMTL conference. I want to encourage the attendees to come to our both so we can explain how they can save money on food and supplies. here is a link to the conference. https://www.brmtl-example.org/conference/ here is our website www.pantrywisehub-example.com - the what we do can be captured in the ad. We will be at booth 505. Our goal is to get people to our booth #505 to explain the services that we provide –

Discounted food pricing
Free menu planning/design
Use of Registered Dietitian
Huge selection of discounted PPE and other necessary supplies to run any child care center

We have over 6000 members in 46 States and work with both small and large food distributors. We have been a sponsor of the association for the last 10 years.

Target Market(s)

Child care centers

Requirements
Must have
• Booth number -outline of what we do --- Stress we are a FREE service getting our members reduced pricing on food and supplies

```html
<!DOCTYPE html>
<html lang="en">
<head>
<meta charset="utf-8">
<title>PantryWise Hub – BRMTL Conference Half Page Ad</title>
<link rel="stylesheet" href="https://fonts.googleapis.com/css2?family=Poppins:ital,wght@0,400;0,600;0,700;1,400&display=swap">
<style>
  :root {
    --backdrop: #bebcbd;
    --paper: #ffffff;
    --brand-blue: #1f7bbb;
    --band-blue: rgba(79, 141, 201, 0.88);
    --ink: #1b1b1b;
    --photo-hero: linear-gradient(100deg, #7c8790 0%, #b3a79a 35%, #d6c2ad 55%, #9fb0bc 80%, #c4b8a8 100%);
    --photo-food: linear-gradient(90deg, #c59a9b 0%, #eef0ef 35%, #f4f4f3 55%, #8c9b50 75%, #d28a3f 100%);
    --photo-child: radial-gradient(circle at 55% 35%, #e7c3ae 0%, #c9a48e 30%, #b9726c 55%, #a6b18d 75%, #e0502e 100%);
  }
  * { margin: 0; padding: 0; box-sizing: border-box; }
  html, body { width: 1200px; height: 1128px; overflow: hidden; background: var(--backdrop); }
  body { position: relative; font-family: "Poppins", sans-serif; color: var(--ink); }

  .ad { position: absolute; left: 75px; top: 226px; width: 1049px; height: 680px; background: var(--paper); overflow: hidden; }

  .hero-photo { position: absolute; left: 0; top: 0; width: 1049px; height: 288px; background: var(--photo-hero); }
  .corner-curve { position: absolute; left: 0; top: 0; width: 90px; height: 75px; }

  .hero-band { position: absolute; left: 0; top: 31px; width: 1049px; height: 161px; background: var(--band-blue); color: #fff; }
  .event-title { position: absolute; left: 66px; top: 8px; font-size: 26px; font-weight: 400; line-height: 32px; white-space: nowrap; }
  .event-meta { position: absolute; left: 66px; top: 40px; font-size: 23px; font-style: italic; line-height: 28px; }
  .headline { position: absolute; left: 66px; top: 117px; font-size: 23px; font-weight: 700; letter-spacing: 0.1px; white-space: nowrap; }

  .brand-pill { position: absolute; left: 765px; top: 46px; width: 300px; height: 66px; background: var(--paper); border-radius: 20px 0 0 20px; display: flex; align-items: center; gap: 10px; padding-left: 20px; }
  .brand-mark { width: 20px; height: 20px; background: var(--brand-blue); }
  .brand-name { font-size: 21px; font-weight: 400; color: #555; }

  .food-photo { position: absolute; left: 436px; top: 317px; width: 370px; height: 137px; border-radius: 70px 0 0 70px; background: var(--photo-food); }

  .child-ring { position: absolute; left: 789px; top: 207px; width: 330px; height: 314px; border-radius: 50%; background: var(--paper); }
  .child-photo { position: absolute; left: 795px; top: 215px; width: 316px; height: 300px; border-radius: 50%; background: var(--photo-child); }

  .invite { position: absolute; left: 59px; top: 314px; width: 340px; font-size: 19.5px; line-height: 22.7px; }
  .invite strong { color: var(--brand-blue); font-weight: 700; }

  .benefits { position: absolute; left: 0; top: 492px; width: 1049px; list-style: none; }
  .benefit { position: absolute; top: 0; font-size: 17.5px; line-height: 20.5px; }
  .benefit svg { display: block; width: 27px; height: 27px; margin-bottom: 7px; margin-left: -1px; }
  .benefit:nth-child(1) { left: 58px; }
  .benefit:nth-child(2) { left: 239px; }
  .benefit:nth-child(3) { left: 441px; }
  .benefit:nth-child(4) { left: 609px; width: 300px; }

  .footer-band { position: absolute; left: 0; top: 609px; width: 1049px; height: 71px; background: var(--brand-blue); color: #fff; }
  .footer-facts { position: absolute; left: 59px; top: 10px; font-size: 17px; line-height: 20.5px; white-space: nowrap; }
  .footer-url { position: absolute; right: 31px; top: 11px; font-size: 13px; font-weight: 700; white-space: nowrap; }
</style>
</head>
<body>
<main class="ad">
  <div class="hero-photo" role="img" aria-label="Photo of a young girl biting into a large lettuce sandwich"></div>
  <svg class="corner-curve" viewBox="0 0 90 75" aria-hidden="true"><path d="M0 0 H88 Q50 60 0 72 Z" fill="#fff"/></svg>

  <section class="hero-band">
    <h1 class="event-title">2022 BRMTL Child Nutrition Conference</h1>
    <p class="event-meta">April 18-22, 2022<br>New Orleans, Louisiana</p>
    <h2 class="headline">PANTRYWISE HUB CONSULTANTS ARE MONEY-SAVING EXPERTS.</h2>
  </section>

  <div class="brand-pill">
    <span class="brand-mark"></span>
    <span class="brand-name">PantryWise Hub</span>
  </div>

  <div class="food-photo" role="img" aria-label="Photo of a bowl of roasted vegetables with quinoa, limes and herbs"></div>
  <div class="child-ring"></div>
  <div class="child-photo" role="img" aria-label="Photo of a smiling girl in a striped shirt with a bowl of berries"></div>

  <p class="invite"><strong>Join us at booth 505</strong> to learn about the great benefits we Offer ! We'll analyze your current food and supply purchases and find ways for you to save - <strong>Free of charge.</strong></p>

  <ul class="benefits">
    <li class="benefit"><svg viewBox="0 0 27 27" aria-hidden="true"><circle cx="13.5" cy="13.5" r="13.5" fill="#1f7bbb"/><path d="M7.5 14 L12 18.5 L19.5 9.5" fill="none" stroke="#fff" stroke-width="3" stroke-linecap="round" stroke-linejoin="round"/></svg>Discounted<br>food pricing</li>
    <li class="benefit"><svg viewBox="0 0 27 27" aria-hidden="true"><circle cx="13.5" cy="13.5" r="13.5" fill="#1f7bbb"/><path d="M7.5 14 L12 18.5 L19.5 9.5" fill="none" stroke="#fff" stroke-width="3" stroke-linecap="round" stroke-linejoin="round"/></svg>Free menu<br>planning/design</li>
    <li class="benefit"><svg viewBox="0 0 27 27" aria-hidden="true"><circle cx="13.5" cy="13.5" r="13.5" fill="#1f7bbb"/><path d="M7.5 14 L12 18.5 L19.5 9.5" fill="none" stroke="#fff" stroke-width="3" stroke-linecap="round" stroke-linejoin="round"/></svg>Use of<br>Registered<br>Dietitian</li>
    <li class="benefit"><svg viewBox="0 0 27 27" aria-hidden="true"><circle cx="13.5" cy="13.5" r="13.5" fill="#1f7bbb"/><path d="M7.5 14 L12 18.5 L19.5 9.5" fill="none" stroke="#fff" stroke-width="3" stroke-linecap="round" stroke-linejoin="round"/></svg>Huge selection of discounted PPE<br>and other necessary supplies to<br>run any child care center</li>
  </ul>

  <footer class="footer-band">
    <p class="footer-facts">We have over 6000 members in 46 States and work with both small and large<br>food distributors. We have been a sponsor of the association for the last 10 years</p>
    <p class="footer-url">www.pantrywisehub-example.com</p>
  </footer>
</main>
</body>
</html>
```